Copper Lantern Fitness Flyer

We need a Flyer designed for a Revolutionary Fresh New Functional Fitness facility in Manly Sydney, Australia. We have just recently opened and now need to get the word out. Using the flyers to hand out at events also for shop counters and letterbox drops.

Our company name is Copper Lantern Fitness "Where STRENGTH Becomes Your SPARK".
We promote health and fitness to all fitness levels concentrating on functional fitness. To learn more about us and our colour scheme see attached file and also check us out on www.brightvine-social.example/copperlanternfitnessgroup

A5 Size please

Target Market(s)

The beauty of our system is it is for everyone we have girls and guys in there teens, 20's 30's 40's and 50's. Not only that we have professional athletes, military and high fitness levels all the way to people who are overweight and need to loose weight and tone up. The system caters for everyone.

Industry/Entity Type

Fitness

Requirements
Must have
• FRONT:

Free 30min Fat Blasting Experience With Your Very Own Personal Trainer !!!

New Class Starts Every 3 minutes.
30 minute Workout With A Trainer.
No Machines No Mirrors And No Attitudes.
Catering For All Fitness Levels.
Results Guaranteed Or Your Money Back.
Fun, Fresh, Clean, Revolutionary New Facility.

Back:

You Are Just Moments Away From Burning Fat Faster Than Ever Before And Getting That Body You Always Wanted !!!

Come In Today To Claim Your FREE Workout.

Ph (02) 9417 2086
Address 5/127 Greywattle Ave Fernbrook 2178
www.brightvine-social.example/copperlanternfitnessgroup
Nice to have
• FRONT:

Back:

Ph (02) 9417 2086

```html
<!DOCTYPE html>
<html lang="en">
<head>
<meta charset="utf-8">
<title>Copper Lantern Fitness Flyer</title>
<link rel="stylesheet" href="https://fonts.googleapis.com/css2?family=Anton&display=swap">
<style>
  :root {
    --navy: #0b1a86;
    --navy-deep: #07125f;
    --band-blue: #1f45d6;
    --band-blue-light: #2f62f0;
    --gold: #e2b93a;
    --gold-light: #f6dc7a;
    --gold-dark: #a8801c;
    --mark-fill: #3f63e6;
    --white: #ffffff;
    --shadow: #000000;
  }
  html, body {
    margin: 0;
    padding: 0;
    overflow: hidden;
    background: var(--navy);
  }
  .flyer {
    position: relative;
    width: 1200px;
    height: 900px;
    overflow: hidden;
    background: var(--navy);
    font-family: "Anton", "Arial Narrow", sans-serif;
  }
  .hero-photo {
    position: absolute;
    left: 150px;
    top: 0;
    width: 700px;
    height: 330px;
    background:
      radial-gradient(ellipse 30% 90% at 32% 20%, #122070 0%, rgba(18,32,112,0) 100%),
      radial-gradient(ellipse 30% 90% at 72% 20%, #122070 0%, rgba(18,32,112,0) 100%),
      linear-gradient(180deg, #0d1a78 0%, #0b1a86 100%);
  }
  .brand-mark {
    position: absolute;
    left: 92px;
    top: 88px;
    width: 190px;
    height: 190px;
    background: var(--mark-fill);
  }
  .brand-name {
    position: absolute;
    right: 88px;
    top: 60px;
    margin: 0;
    text-align: right;
    font-weight: 400;
    font-size: 60px;
    line-height: 62px;
    letter-spacing: 8px;
    color: var(--gold);
    text-transform: uppercase;
  }
  .band {
    position: absolute;
    left: 0;
    top: 0;
    width: 1200px;
    height: 900px;
  }
  .feature-list {
    position: absolute;
    left: 80px;
    top: 340px;
    margin: 0;
    padding: 0;
    list-style: none;
    color: var(--white);
    font-size: 40px;
    line-height: 50px;
    letter-spacing: 1.2px;
    text-transform: uppercase;
    text-shadow: 3px 3px 0 var(--shadow), 0 0 4px var(--shadow);
  }
  .offer {
    position: absolute;
    left: 0;
    top: 738px;
    width: 1200px;
    margin: 0;
    text-align: center;
    font-weight: 400;
    font-size: 66px;
    line-height: 70px;
    letter-spacing: 0.8px;
    text-transform: uppercase;
    color: var(--gold);
    background: linear-gradient(180deg, var(--gold-light) 0%, var(--gold) 50%, var(--gold-dark) 100%);
    -webkit-background-clip: text;
    background-clip: text;
    -webkit-text-fill-color: transparent;
    filter: drop-shadow(4px 4px 0 var(--shadow));
  }
</style>
</head>
<body>
<main class="flyer">
  <div class="hero-photo" role="img" aria-label="Dark photo of two athletes' toned torsos in silhouette"></div>

  <div class="brand-mark" role="img" aria-label="Brand mark"></div>

  <h1 class="brand-name">Copper<br>Lantern<br>Fitness</h1>

  <svg class="band" viewBox="0 0 1200 900" xmlns="http://www.w3.org/2000/svg">
    <defs>
      <linearGradient id="bandBlue" x1="0" y1="0" x2="1" y2="0">
        <stop offset="0" stop-color="#2f62f0"/>
        <stop offset="1" stop-color="#1f45d6"/>
      </linearGradient>
      <linearGradient id="gymTones" x1="0" y1="0" x2="0" y2="1">
        <stop offset="0" stop-color="#d9dbe0"/>
        <stop offset="0.22" stop-color="#b8bcc4"/>
        <stop offset="0.36" stop-color="#5a5e66"/>
        <stop offset="0.55" stop-color="#2e3136"/>
        <stop offset="1" stop-color="#24272b"/>
      </linearGradient>
      <radialGradient id="turf" cx="1" cy="0.85" r="0.45">
        <stop offset="0" stop-color="#3f9a35"/>
        <stop offset="1" stop-color="#3f9a35" stop-opacity="0"/>
      </radialGradient>
      <clipPath id="waveClip">
        <path d="M0 322 C 120 345, 260 350, 420 318 C 640 275, 900 262, 1200 272 L 1200 640 C 980 690, 760 712, 520 700 C 320 690, 150 678, 0 688 Z"/>
      </clipPath>
    </defs>
    <g clip-path="url(#waveClip)">
      <rect x="0" y="250" width="1200" height="480" fill="url(#bandBlue)"/>
      <g role="img" aria-label="Photo of the training floor with spin bikes, step platforms, kettlebells and wall posters">
        <path d="M470 250 L 1200 250 L 1200 730 L 560 730 C 520 600, 420 470, 470 250 Z" fill="url(#gymTones)"/>
        <path d="M470 250 L 1200 250 L 1200 730 L 560 730 C 520 600, 420 470, 470 250 Z" fill="url(#turf)"/>
      </g>
    </g>
    <path d="M0 322 C 120 345, 260 350, 420 318 C 640 275, 900 262, 1200 272" fill="none" stroke="var(--gold)" stroke-width="5"/>
    <path d="M0 688 C 150 678, 320 690, 520 700 C 760 712, 980 690, 1200 640" fill="none" stroke="var(--gold)" stroke-width="5"/>
  </svg>

  <ul class="feature-list">
    <li>New class starts every 3 minutes.</li>
    <li>30 minute workout with a trainer</li>
    <li>No machines no mirrors and no attitudes.</li>
    <li>Catering for all fitness levels.</li>
    <li>Results guaranteed or your money back.</li>
    <li>Fun, fresh, clean, revolutionary new facility.</li>
  </ul>

  <h2 class="offer">Free 30min fat blasting experience<br>with your very own personal trainer!!!</h2>
</main>
</body>
</html>
```